B2B Umbrella Site Requires Simple, Stylish Slider Designs

We're a dynamic promotional merchandise business in the process of building a new B2B Umbrella Store. It's our goal to provide printed umbrellas to suit the needs of our clients. Our main page is in need of ONE large key banner and THREE smaller sub category banners. We would like to see designs that use grey and green (or similar) to match with the theme of our layout. See: http://canopyvault.com.au/

The final designs should convey the desirability of our umbrellas while looking slick and modern in style. Please find attached our place holder banners for size reference and umbrella images to use in designs. If you require any further details or content, feel free to contact us.

Target Market(s)

Professionals and businesses across a wide range of fields. We offer a customisable product so we are as flexible as our target market.

Industry/Entity Type

Building

Font styles to use
Sans Serif

Requirements
Must have
• Must match sizes of attached sample graphics (
sub_banner + main_banner images). Must feature umbrella images attached to the brief - pick which images suit your design, but please ensure they are the correct umbrella style for the banner text. Clear, stylish text based on existing text found on sample graphics.
Nice to have
• Colours similar to the ones existing on the website already.
Should not have
• No serif fonts or clipart. Colours that do not facilitate easy reading.

```html
<!DOCTYPE html>
<html lang="en">
<head>
<meta charset="utf-8">
<title>CanopyVault – Promotional Umbrellas</title>
<link rel="stylesheet" href="https://fonts.googleapis.com/css2?family=Roboto:wght@400;500;700&family=Montserrat:wght@400;500;700;800&display=swap">
<style>
  :root {
    --green: #78c000;
    --green-dark: #5e9e00;
    --green-light: #92cf00;
    --blue: #0d6e9e;
    --ink: #1b1b1b;
    --text: #444444;
    --muted: #8a8a8a;
    --line: #d9d9d9;
    --panel: #ffffff;
    --page: #f4f4f4;
    --btn-dark: #3a3a3a;
    --sky-top: #5cc8ec;
    --sky-bottom: #b8e8f6;
    --sub-top: #8fcf1c;
    --sub-bottom: #e9f3cf;
    --note: #e8e8e8;
  }
  * { box-sizing: border-box; margin: 0; padding: 0; }
  html, body { width: 1200px; height: 730px; overflow: hidden; }
  body { background: var(--page); font-family: "Roboto", Arial, sans-serif; position: relative; color: var(--text); }

  .site-header {
    position: absolute; left: 15px; top: 13px; width: 1200px; height: 174px;
    background: var(--panel); border: 1px solid var(--line); border-radius: 6px;
  }
  .brand { position: absolute; left: 30px; top: 40px; display: flex; align-items: center; gap: 10px; }
  .brand-name { font-weight: 700; font-size: 36px; color: var(--green-dark); letter-spacing: -0.5px; }
  .brand-dot { width: 22px; height: 22px; border-radius: 50%; background: var(--blue); }

  .search { position: absolute; left: 916px; top: 25px; display: flex; gap: 4px; }
  .search-input { width: 184px; height: 32px; border: 1px solid var(--line); border-radius: 4px; background: #fff; }
  .search-button {
    width: 78px; height: 33px; border-radius: 4px; background: var(--btn-dark);
    color: #fff; font-size: 13px; display: flex; align-items: center; justify-content: center;
  }

  .main-nav {
    position: absolute; left: 30px; top: 98px; width: 1150px; height: 46px;
    background: linear-gradient(var(--green-light), var(--green) 60%, var(--green-dark));
    border-radius: 3px; display: flex; box-shadow: 0 2px 3px rgba(0,0,0,.15);
  }
  .nav-item {
    color: #fff; font-size: 15px; font-weight: 400; padding: 0 19px;
    display: flex; align-items: center; border-right: 1px solid rgba(255,255,255,.55);
  }

  .content {
    position: absolute; left: 15px; top: 190px; width: 1200px; height: 560px;
    background: var(--panel); border: 1px solid var(--line); border-radius: 6px;
  }

  .sidebar-heading {
    position: absolute; left: 45px; width: 265px; height: 45px;
    border: 1px solid var(--line); border-radius: 3px; background: #fff;
    box-shadow: 0 2px 3px rgba(0,0,0,.12);
    font-size: 18px; color: #555; padding: 9px 18px;
  }
  .categories-heading { top: 218px; }
  .enquiry-heading { top: 546px; }
  .category-list { position: absolute; left: 51px; top: 300px; width: 252px; list-style: none; }
  .category-list li {
    height: 37.5px; font-size: 12px; font-weight: 500; color: #333;
    border-bottom: 1px dotted #b5b5b5; padding-top: 8px;
  }
  .field-label { position: absolute; left: 51px; font-size: 12px; color: var(--muted); }
  .field-input { position: absolute; left: 51px; width: 254px; height: 32px; border: 1px solid #ccc; border-radius: 4px; background: #fff; }

  .hero-banner {
    position: absolute; left: 340px; top: 218px; width: 856px; height: 350px;
    border: 1px solid var(--line); background: #fff; overflow: hidden;
    font-family: "Montserrat", Arial, sans-serif; color: var(--ink);
  }
  .hero-banner > * { position: absolute; left: 52px; white-space: nowrap; }
  .hero-kicker { top: 17px; height: 34px; line-height: 34px; font-size: 27px; color: var(--blue); }
  .hero-kicker strong { font-weight: 700; }
  .hero-rule { width: 365px; height: 2px; background: var(--ink); }
  .hero-rule.upper { top: 76px; }
  .hero-rule.lower { top: 178px; }
  .hero-title { top: 84px; height: 44px; line-height: 44px; font-size: 40px; font-weight: 800; letter-spacing: 0.3px; }
  .hero-subtitle { top: 132px; height: 40px; line-height: 40px; font-size: 33px; font-weight: 400; letter-spacing: 0.3px; }
  .hero-tags { top: 188px; height: 16px; line-height: 16px; font-size: 11.5px; }
  .hero-offer { top: 212px; font-size: 22px; line-height: 36px; }
  .hero-offer strong { color: var(--green); font-weight: 700; }

  .hero-photo.hero-photo {
    left: 460px; top: 14px; width: 380px; height: 321px;
    background: linear-gradient(var(--sky-top), var(--sky-bottom));
  }
  .catalog-button.catalog-button {
    left: 340px; top: 274px; width: 165px; height: 36px;
    background: var(--blue); color: #fff; border: 2px solid #fff;
    font-size: 19px; font-weight: 500; line-height: 32px; text-align: center;
  }

  .sub-banner {
    position: absolute; top: 568px; width: 280px; height: 154px; overflow: hidden;
    background: linear-gradient(var(--sub-top), #b9e05a 55%, var(--sub-bottom));
    border: 1px solid var(--line); font-family: "Montserrat", Arial, sans-serif; color: var(--ink);
  }
  .sub-photo { position: absolute; left: 4px; top: 12px; width: 130px; height: 130px; }
  .sub-band { position: absolute; left: 0; top: 84px; width: 280px; height: 26px; background: var(--blue); }
  .sub-copy { position: absolute; right: 12px; top: 25px; text-align: right; }
  .sub-kicker { font-size: 9.5px; line-height: 13px; }
  .sub-title { font-size: 21px; font-weight: 800; letter-spacing: 1.5px; line-height: 22px; }
  .sub-line { font-size: 18px; font-weight: 500; letter-spacing: 1px; line-height: 20px; }
  .sub-line.spaced { letter-spacing: 5px; }
  .sub-line.wide { letter-spacing: 11px; margin-right: -11px; }
  .sub-band-label {
    position: absolute; right: 12px; top: 84px; height: 26px; line-height: 26px; color: #fff;
    font-size: 19px; font-weight: 500; letter-spacing: 0.5px;
  }
  .sub-footer { position: absolute; right: 12px; bottom: 8px; display: flex; font-size: 9.5px; font-family: "Roboto", Arial, sans-serif; }
  .sub-footer-note { background: var(--note); color: #333; padding: 2px 6px; }
  .sub-footer-cta { background: var(--ink); color: #fff; font-weight: 700; padding: 2px 7px; }
</style>
</head>
<body>
  <header class="site-header">
    <div class="brand"><span class="brand-name">CanopyVault</span><span class="brand-dot"></span></div>
    <div class="search"><div class="search-input"></div><div class="search-button">Search</div></div>
    <nav class="main-nav">
      <span class="nav-item">Home</span>
      <span class="nav-item">Fast Delivery</span>
      <span class="nav-item">Testimonials</span>
      <span class="nav-item">Sampling</span>
      <span class="nav-item">Contact Us</span>
      <span class="nav-item">FAQ</span>
    </nav>
  </header>

  <main class="content"></main>

  <aside>
    <div class="sidebar-heading categories-heading">Categories</div>
    <ul class="category-list">
      <li>Childrens Umbrellas</li>
      <li>Folding Umbrellas</li>
      <li>Medium Umbrellas</li>
      <li>Big Golf Umbrellas</li>
      <li>Beach Umbrellas</li>
      <li>Cafe Umbrellas</li>
    </ul>
    <div class="sidebar-heading enquiry-heading">Enquiry</div>
    <span class="field-label" style="top:638px">Name:</span>
    <div class="field-input" style="top:669px"></div>
    <span class="field-label" style="top:713px">Phone:</span>
  </aside>

  <section class="hero-banner">
    <p class="hero-kicker">AUSTRALIA’S <strong>TOP</strong></p>
    <div class="hero-rule upper"></div>
    <h1 class="hero-title">PROMOTIONAL</h1>
    <p class="hero-subtitle">UMBRELLA VENDOR</p>
    <div class="hero-rule lower"></div>
    <p class="hero-tags">Huge Range | Fast Delivery | Great Prices | Amazing Colours</p>
    <p class="hero-offer"><strong>Now!</strong> Get Custom Printed<br>Umbrellas With Your Logo</p>
    <div class="hero-photo" role="img" aria-label="Photo of a black and white promotional golf umbrella on a sky blue background"></div>
    <span class="catalog-button">View Catalog</span>
  </section>

  <section class="sub-banner" style="left:342px">
    <div class="sub-photo" role="img" aria-label="Photo of a yellow medium umbrella" style="background:radial-gradient(circle, #f2d33c, rgba(242,211,60,0) 70%)"></div>
    <div class="sub-band"></div>
    <div class="sub-copy">
      <p class="sub-kicker">— Huge Range of —</p>
      <p class="sub-title">MEDIUM</p>
      <p class="sub-line">CORPORATE</p>
    </div>
    <span class="sub-band-label">UMBRELLAS</span>
    <div class="sub-footer"><span class="sub-footer-note">For Fast Delivery</span><span class="sub-footer-cta">Order Now</span></div>
  </section>

  <section class="sub-banner" style="left:626px">
    <div class="sub-photo" role="img" aria-label="Photo of a purple folding umbrella" style="background:radial-gradient(circle, #a98be6, rgba(169,139,230,0) 70%)"></div>
    <div class="sub-band"></div>
    <div class="sub-copy">
      <p class="sub-kicker">— Great Prices of —</p>
      <p class="sub-title">PORTABLE</p>
      <p class="sub-line spaced">FOLDING</p>
    </div>
    <span class="sub-band-label">UMBRELLAS</span>
    <div class="sub-footer"><span class="sub-footer-note">For Fast Delivery</span><span class="sub-footer-cta">Order Now</span></div>
  </section>

  <section class="sub-banner" style="left:909px">
    <div class="sub-photo" role="img" aria-label="Photo of a red golf umbrella" style="background:radial-gradient(circle, #d81818, rgba(216,24,24,0) 70%)"></div>
    <div class="sub-band"></div>
    <div class="sub-copy">
      <p class="sub-kicker">— Amazing Colors of —</p>
      <p class="sub-title">POPULAR</p>
      <p class="sub-line wide">GOLF</p>
    </div>
    <span class="sub-band-label">UMBRELLAS</span>
    <div class="sub-footer"><span class="sub-footer-note">For Fast Delivery</span><span class="sub-footer-cta">Order Now</span></div>
  </section>
</body>
</html>
```